Year End Gift for Employees

Looking for assistance in creating an album cover. Here are some ideas that I have: Double Platinum, Copper Lantern Drift, 2025 World Tour
TK/RV (name of the band) – on the front of the album cover
List of Songs - on the back of the album cover
Would like to have the ability to have team / individual pictures on the inside of the double platinum album cover
DON’T want anything gory or vulgar for the album cover
Also want rights to the image for the album cover to use for t-shirts
This is a Sales Team that work within Maplecrest Building Supply
Any additional images that you want to propose, I'm open too. Thanks and I'll await your response
Colleagues

```html
<!DOCTYPE html>
<html lang="en">
<head>
<meta charset="utf-8">
<title>TK/RV 2025 World Tour – Album &amp; Shirt Set</title>
<link rel="stylesheet" href="https://fonts.googleapis.com/css2?family=Oswald:wght@400;700&family=Allura&family=Pirata+One&display=swap">
<style>
  :root {
    --stage: #d9d9d9;
    --steel-light: #e6ecf3;
    --steel-mid: #b3c0cf;
    --steel-dark: #7f90a5;
    --steel-ink: #8d9db0;
    --ink: #1b1d22;
    --band-red: #d0141a;
    --photo-grey: #a3a5aa;
    --photo-label: #c4c6ca;
    --frame-white: #ffffff;
    --torn-dark: #1f2228;
    --shirt-black: #111113;
    --print-steel: #a9b8c9;
    --print-white: #f2f2f2;
    --date-blue: #a8b7d4;
  }
  * { box-sizing: border-box; margin: 0; padding: 0; }
  html, body { width: 1200px; height: 541px; overflow: hidden; }
  body { background: var(--stage); position: relative; font-family: "Oswald", sans-serif; }

  .steel {
    position: absolute;
    overflow: hidden;
    background:
      repeating-linear-gradient(0deg, rgba(255,255,255,.10) 0 1px, rgba(0,0,0,.04) 1px 2px),
      conic-gradient(from 45deg at 55% 50%, var(--steel-mid), var(--steel-light), var(--steel-dark), var(--steel-light), var(--steel-mid), var(--steel-light), var(--steel-dark), var(--steel-light), var(--steel-mid));
  }
  .album-front { left: 26px; top: 28px; width: 229px; height: 229px; }
  .album-back  { left: 280px; top: 28px; width: 230px; height: 229px; }
  .album-inside{ left: 280px; top: 277px; width: 230px; height: 229px; }
  .disc { left: 27px; top: 282px; width: 228px; height: 228px; border-radius: 50%; }
  .disc-hole { position: absolute; left: 94px; top: 94px; width: 38px; height: 38px; border-radius: 50%; background: var(--stage); }

  .band-mark {
    position: absolute; left: 0; width: 100%; text-align: center; white-space: nowrap;
    font-family: "Oswald", sans-serif; font-weight: 700; line-height: 1;
    color: var(--steel-ink); letter-spacing: 1px;
    transform-origin: top center;
  }
  .album-front .band-mark { font-size: 72px; transform: scaleY(1.15); }
  .album-front .mark-top { top: 2px; }
  .album-front .mark-bottom { top: 122px; }
  .tour-script { position: absolute; font-family: "Allura", cursive; color: var(--ink); white-space: nowrap; line-height: 1; }
  .album-front .tour-script { left: 0; width: 100%; text-align: center; top: 105px; font-size: 21px; }

  .disc .band-mark { font-size: 56px; transform: scaleY(1.5); }
  .disc .mark-top { top: 16px; }
  .disc .mark-bottom { top: 116px; }
  .disc .tour-script { left: 134px; top: 98px; width: 84px; font-size: 18px; line-height: .9; text-align: center; }

  .back-title {
    position: absolute; top: 4px; left: 0; width: 100%; text-align: center; white-space: nowrap;
    font-family: "Oswald", sans-serif; font-weight: 700; font-size: 19px; line-height: 1;
    color: var(--band-red); letter-spacing: -.2px;
    transform: scaleY(1.25); transform-origin: top center;
  }
  .album-back .tour-script { left: 0; width: 100%; text-align: center; top: 30px; font-size: 16px; }
  .tracklist { position: absolute; list-style: none; text-align: center; font-size: 10px; line-height: 14.6px; color: var(--ink); white-space: nowrap; }
  .tracklist-a { left: 8px; width: 114px; top: 62px; }
  .tracklist-b { left: 118px; width: 108px; top: 68px; }

  .torn-backing { position: absolute; background: var(--torn-dark); }
  .photo-frame { position: absolute; background: var(--frame-white); padding: 4px; }
  .photo-slot {
    width: 100%; height: 100%; background: var(--photo-grey);
    display: flex; align-items: center; justify-content: center;
    font-family: "Oswald", sans-serif; font-weight: 700; color: var(--photo-label);
  }
  .photo-one { left: 21px; top: 26px; width: 118px; height: 87px; }
  .photo-one .photo-slot { font-size: 37px; }
  .photo-two { left: 99px; top: 132px; width: 101px; height: 74px; }
  .photo-two .photo-slot { font-size: 31px; }

  .shirt-print { position: absolute; background: var(--shirt-black); }
  .shirt-front-print { left: 615px; top: 108px; width: 165px; height: 150px; }
  .shirt-front-print .band-mark { color: var(--print-steel); font-size: 50px; transform: scaleY(1.3); }
  .shirt-front-print .mark-top { top: 0; }
  .shirt-front-print .mark-bottom { top: 80px; }
  .shirt-front-print .tour-script { left: 0; width: 100%; text-align: center; top: 68px; font-size: 16px; color: var(--print-white); }

  .shirt-back-print { left: 905px; top: 225px; width: 170px; height: 190px; }
  .tour-dates {
    list-style: none; position: absolute; top: 12px; left: 0; width: 100%; text-align: center; white-space: nowrap;
    font-family: "Pirata One", serif; font-size: 8px; line-height: 17px; color: var(--date-blue);
  }
</style>
</head>
<body>

  <section class="steel album-front" aria-label="Album front cover">
    <div class="band-mark mark-top">TK/RV</div>
    <div class="tour-script">2025 World Tour</div>
    <div class="band-mark mark-bottom">TK/RV</div>
  </section>

  <section class="steel album-back" aria-label="Album back cover">
    <h1 class="back-title">COPPER LANTERN DRIFT</h1>
    <div class="tour-script">2025 World Tour</div>
    <ol class="tracklist tracklist-a">
      <li>1. Song Name</li>
      <li>2. Another Song Name</li>
      <li>3. Song Name</li>
      <li>4. Even Longer Song Name</li>
      <li>5. Song Name</li>
      <li>6. Just a Song Name</li>
      <li>7. One More Song Name</li>
      <li>8. Song Name</li>
      <li>9. Song Name</li>
    </ol>
    <ol class="tracklist tracklist-b">
      <li>10. Song</li>
      <li>11. Maybe Song Name</li>
      <li>12. Pretty Song Name</li>
      <li>13. Another Name</li>
      <li>14. Song Name</li>
      <li>15. Yet anotherSong Name</li>
      <li>16. Song Name</li>
      <li>17. Last Name</li>
    </ol>
  </section>

  <section class="steel disc" aria-label="Disc label">
    <div class="band-mark mark-top">TK/RV</div>
    <div class="band-mark mark-bottom">TK/RV</div>
    <div class="tour-script">2025<br>World Tour</div>
    <div class="disc-hole"></div>
  </section>

  <section class="steel album-inside" aria-label="Album inside panel">
    <div class="torn-backing" role="img" aria-label="Torn dark paper behind team photo" style="left:12px;top:14px;width:128px;height:94px;"></div>
    <div class="photo-frame photo-one">
      <div class="photo-slot" role="img" aria-label="Team photo">PHOTO</div>
    </div>
    <div class="torn-backing" role="img" aria-label="Torn dark paper behind individual photo" style="left:110px;top:140px;width:104px;height:76px;"></div>
    <div class="photo-frame photo-two">
      <div class="photo-slot" role="img" aria-label="Individual photo">PHOTO</div>
    </div>
  </section>

  <section class="shirt-print shirt-front-print" aria-label="T-shirt front print">
    <div class="band-mark mark-top">TK/RV</div>
    <div class="tour-script">2025 World Tour</div>
    <div class="band-mark mark-bottom">TK/RV</div>
  </section>

  <section class="shirt-print shirt-back-print" aria-label="T-shirt back print">
    <ul class="tour-dates">
      <li>Feb 12, 2025 – Seattle, WA</li>
      <li>Mar 03, 2025 – Denver, CO</li>
      <li>Mar 28, 2025 – Austin, TX</li>
      <li>Apr 10, 2025 – New Orleans, LA</li>
      <li>May 02, 2025 – Nashville, TN</li>
      <li>Jun 14, 2025 – Chicago, IL</li>
      <li>Jul 09, 2025 – Toronto, ON</li>
      <li>Aug 21, 2025 – New York, NY</li>
      <li>Sep 18, 2025 – Boston, MA</li>
      <li>Oct 30, 2025 – Los Angeles, CA</li>
    </ul>
  </section>

</body>
</html>
```